Medical Office Needs an Updated Treatment Brochure

We need an updated brochure for a new treatment our offices are offering. The old brochure attached has all the current information on it, it just needs a new design.
We would like the updated version to be more modern and sleek as well as engaging.
Please see the old brochure attached for reference as well as this link: http://www.glimravex.com/medspa/iv-therapy/#1
The content from the attached brochure will remain.
UPDATE**** PLEASE SEE THE ATTACHED EXAMPLE BROCHURE OF THE DESIGN WE ARE LOOKING FOR!!
Thank you!!
Medical

```html
<!DOCTYPE html>
<html lang="en">
<head>
<meta charset="utf-8">
<title>Glimravex IV Nutrient Therapy Brochure</title>
<link href="https://fonts.googleapis.com/css2?family=Oswald:wght@400;500;600&family=Arimo:ital,wght@0,400;0,700;1,400&display=swap" rel="stylesheet">
<style>
:root{
  --green:#a8cf96;
  --green-mid:#8fbf7d;
  --green-dark:#5f7a58;
  --charcoal:#4a4a4a;
  --charcoal-dark:#3d3d3d;
  --ink:#2f2f2f;
  --text:#3a3a3a;
  --white:#ffffff;
  --label:#c9c9c9;
  --rose:#d2708e;
}
*{margin:0;padding:0;box-sizing:border-box}
html,body{width:937px;height:1200px;overflow:hidden;background:var(--white)}
body{position:relative;font-family:"Arimo",Arial,sans-serif;color:var(--text)}
.side-label{position:absolute;font-family:"Arimo",Arial,sans-serif;font-weight:700;font-size:28px;color:var(--label);letter-spacing:.5px}
.sheet{position:absolute;overflow:hidden;box-shadow:0 12px 22px rgba(0,0,0,.28)}
.sheet--inside{left:105px;top:67px;width:731px;height:518px;background:var(--white)}
.sheet--outside{left:101px;top:625px;width:733px;height:519px;background:var(--white)}
.abs{position:absolute}
.heading{font-family:"Oswald",sans-serif;font-weight:500;font-size:16px;color:var(--ink);letter-spacing:.2px;white-space:nowrap}
.pill{position:absolute;font-weight:700;font-size:8px;color:var(--white);padding:0 9px;display:flex;align-items:center;letter-spacing:.2px;white-space:nowrap}
.pill--green{background:var(--green)}
.pill--dark{background:var(--charcoal);border-radius:3px}
.pill--tall{white-space:normal;line-height:10px}
.copy{position:absolute;font-size:8.5px;line-height:10.2px;color:var(--text)}
.copy p{margin-bottom:8px}
.copy b{color:var(--ink)}
.copy--light{color:#f0f0f0}
.photo{position:absolute}
.panel-suite{position:absolute;left:246px;top:0;width:244px;height:518px;background:var(--charcoal)}
.panel-benefit{position:absolute;left:490px;top:0;width:241px;height:518px;background:var(--green)}
.offer{position:absolute;display:flex;align-items:center;gap:7px;font-size:8.5px;color:var(--white);white-space:nowrap}
.offer i{display:block;width:26px;height:26px;border-radius:50%;background:radial-gradient(circle at 40% 35%,#f4f4f4,#9a9a9a);border:1.5px solid #e8e8e8}
.quote-card{position:absolute;background:var(--white);border-radius:8px;font-style:italic;font-size:8px;line-height:10px;color:var(--ink);padding:16px 20px 0 26px}
.quote-mark{position:absolute;font-family:"Oswald",sans-serif;font-weight:600;font-size:30px;line-height:1;color:var(--charcoal-dark)}
.contact{position:absolute;font-size:7.5px;line-height:9.5px;color:#555}
.contact .place{color:var(--rose);font-weight:700;text-transform:uppercase;font-size:7.5px}
.contact-row{display:flex;align-items:center;gap:10px;margin-top:9px}
.contact-row svg{flex:none}
.brand-name{position:absolute;font-family:"Arimo",sans-serif;font-weight:400;font-size:40px;line-height:1;color:var(--green-mid);letter-spacing:-.5px;white-space:nowrap}
.rule{position:absolute;height:1px;background:#bdbdbd}
.title{position:absolute;font-family:"Oswald",sans-serif;font-weight:600;font-size:23px;line-height:1;color:var(--ink);letter-spacing:0;white-space:nowrap}
.tagline{position:absolute;font-size:8.3px;line-height:1;color:#555;letter-spacing:.3px;white-space:nowrap}
</style>
</head>
<body>

<div class="side-label" style="left:424px;top:26px">open</div>

<section class="sheet sheet--inside" aria-label="Brochure inside spread">
  <!-- Ingredients panel -->
  <h2 class="heading abs" style="left:22px;top:22px">INGREDIENTS</h2>
  <div class="pill pill--green" style="left:7px;top:52px;width:92px;height:17px">WHAT'S IN IT?</div>
  <div class="copy" style="left:22px;top:79px;width:200px">A number of nutrients play well-defined roles in the maintenance of a robust immune response, optimal energy, and overall health.</div>
  <div class="pill pill--green" style="left:7px;top:125px;width:223px;height:18px">SOME OF THE AMAZING VITAMINS WE USE:</div>
  <div class="copy" style="left:22px;top:156px;width:198px">
    <p><b>Magnesium:</b> Many people are lacking in this essential mineral. Magnesium is an excellent therapy for patients with heart disease, respiratory problems, migraines, and more. It helps with arrhythmias and can arrest an acute asthma attack. IV magnesium is also very relaxing, something we could all use.</p>
    <p><b>Vitamin C:</b> IV administration fights off foreign invaders in your body and acts as a potent anti-histamine. From infections to cancer, the evidence of its powerful influence is simply astonishing when administered IV and in doses far too high for oral intake.</p>
    <p><b>Glutathione:</b> This is the major super-antioxidant and detoxifying agent of our body. It cannot be taken orally but is made in the body. Whey protein and other nutritionals can help build glutathione in the body. It is severely depleted by mercury and chemicals. Many people exist with glutathione deficiency.</p>
  </div>
  <svg class="abs" style="left:0;top:400px" width="246" height="118" viewBox="0 0 246 118" aria-hidden="true">
    <path d="M0 30 C90 -5 190 40 225 118 L200 118 C165 60 90 30 0 55 Z" fill="var(--green-dark)"/>
    <path d="M0 70 C70 50 135 75 165 118 L145 118 C115 85 60 75 0 88 Z" fill="var(--green)"/>
    <path d="M0 100 C30 98 55 105 70 118 L0 118 Z" fill="var(--green)"/>
  </svg>

  <!-- Therapeutic suite panel -->
  <div class="panel-suite">
    <div class="photo" role="img" aria-label="Photo of a smiling couple in sportswear outdoors beside an IV drip bag filled with fresh fruit" style="left:0;top:0;width:244px;height:213px;background:linear-gradient(180deg,#c9d3dc 0%,#dfe5e8 40%,#8fa863 70%,#6c8a3e 100%)"></div>
    <div class="pill pill--green" style="left:7px;top:234px;width:143px;height:16px;border-radius:2px">OUR THERAPEUTIC SUITE</div>
    <div class="copy copy--light" style="left:20px;top:258px;width:210px">When you receive treatment with IV nutrients, you sit comfortably in a recliner while a sterile IV line is started and your specific composition of nutrients is infused. During this time, which usually lasts less than 50 minutes, you may opt for Plug in you PDA or LapTop and go to work, read, watch TV, nap, or simply relax. A complete treatment course often requires a series of IV infusions.</div>
    <div class="pill pill--green" style="left:7px;top:354px;width:100px;height:16px;border-radius:2px">WHAT WE OFFER</div>
    <div class="offer" style="left:22px;top:380px"><i role="img" aria-label="Diamond icon"></i>GLAMOUR</div>
    <div class="offer" style="left:128px;top:380px"><i role="img" aria-label="Energy icon"></i>ENERGY</div>
    <div class="offer" style="left:22px;top:413px"><i role="img" aria-label="Caduceus icon"></i>IMMUNITY</div>
    <div class="offer" style="left:128px;top:413px"><i role="img" aria-label="Water drop icon"></i>HYDRATION</div>
    <div class="offer" style="left:22px;top:446px"><i role="img" aria-label="Scale icon"></i>WEIGHT LOSS</div>
    <div class="offer" style="left:128px;top:446px"><i role="img" aria-label="Fruit icon"></i>DETOX</div>
    <div class="offer" style="left:22px;top:478px"><i role="img" aria-label="Bottle icon"></i>HANGOVER</div>
    <div class="offer" style="left:128px;top:478px"><i role="img" aria-label="Capsules icon"></i>GLUTATHIONE</div>
  </div>

  <!-- Benefits panel -->
  <div class="panel-benefit">
    <div class="quote-card" style="left:21px;top:38px;width:181px;height:54px">“...Super doses can be administered via IV without gastrointestinal side effects...”</div>
    <div class="quote-mark" style="left:28px;top:28px">“</div>
    <div class="quote-mark" style="left:172px;top:82px">”</div>
    <h2 class="heading abs" style="left:22px;top:116px">WHY IT'S BENEFICIAL</h2>
    <div class="pill pill--dark" style="left:10px;top:149px;width:152px;height:16px">DIRECTLY TO THE SOURCE</div>
    <div class="copy" style="left:22px;top:173px;width:200px">When vitamins, minerals, and other nutrients are infused intravenously (IV) they go directly into your bloodstream to fuel your cells. That means they avoid the potential loss of potency and poor absorption in the gastrointestinal (GI) tract that is a characteristic of nutrients taken orally. This makes IV nutrient administration a powerful therapy for numerous health concerns. In addition, Super doses can be administered via IV without gastrointestinal side effects, which can limit dosing. A perfect example of this is vitamin C, which can only be taken in fairly small amounts orally before causing stomach upset. In contrast, Super doses of vitamin C, which can be very beneficial for the immune system, can be administered safely and without stomach side effects with an intravenous delivery route.</div>
    <div class="pill pill--dark pill--tall" style="left:10px;top:369px;width:198px;height:29px">USE IV THERAPY TO OPTIMIZE<br>YOUR HEALTH</div>
    <div class="copy" style="left:22px;top:408px;width:200px"><b>Proactive:</b> Even if you're healthy, IV administration of a wide range of vitamins and minerals is an extremely effective way to boost your nutritional status, accelerate your athletic performance and prevent illness. It is especially important when flu season is around, or before and during stressful situations.</div>
  </div>
</section>

<section class="sheet sheet--outside" aria-label="Brochure outside spread">
  <!-- Facts panel -->
  <h2 class="heading abs" style="left:18px;top:28px">THE FACTS</h2>
  <div class="pill pill--dark" style="left:8px;top:57px;width:122px;height:15px">WHAT IS IV THERAPY?</div>
  <div class="copy" style="left:18px;top:84px;width:195px">
    <p>IV Nutrient Therapy involves the direct administration of vital minerals, nutrients and vitamins directly into the bloodstream (intravenously infused) through an IV drip.</p>
    <p>These essential nutrients can help boost immune function, increase energy levels, assist in weight management, avoid chronic health issues, and even aid in skin rejuvenation.</p>
  </div>
  <div class="photo" role="img" aria-label="Photo of a smiling medical team in scrubs and white coats" style="left:0;top:204px;width:241px;height:125px;background:linear-gradient(180deg,#f4f4f4 0%,#c9cfd6 45%,#7f9bb8 100%)"></div>
  <svg class="abs" style="left:0;top:300px" width="241" height="219" viewBox="0 0 241 219" aria-hidden="true">
    <path d="M0 20 C70 35 160 30 241 0 L241 219 L0 219 Z" fill="var(--green)"/>
    <path d="M0 15 C80 28 170 20 241 -5 L241 5 C170 30 80 38 0 25 Z" fill="var(--green-dark)"/>
    <path d="M30 219 C80 180 170 170 241 175 L241 185 C170 182 90 190 50 219 Z" fill="var(--green-dark)"/>
  </svg>
  <div class="quote-card" style="left:30px;top:388px;width:181px;height:48px;background:var(--charcoal);color:#eee;font-size:7.5px;padding:12px 14px 0 24px">"IV Therapy is great for boosting health and preventing illness."</div>
  <div class="quote-mark" style="left:40px;top:372px;color:var(--charcoal);font-size:24px">“</div>
  <div class="quote-mark" style="left:198px;top:430px;color:var(--charcoal);font-size:24px">”</div>

  <!-- Cover photography -->
  <div class="photo" role="img" aria-label="Dark teal abstract background of rounded tiles" style="left:241px;top:0;width:245px;height:300px;background:linear-gradient(135deg,#0d2c33 0%,#1a4a52 50%,#081c20 100%)"></div>
  <div class="photo" role="img" aria-label="Soft-focus photo of an IV drip bottle and colourful capsules" style="left:486px;top:0;width:247px;height:300px;background:linear-gradient(160deg,#a9b8c6 0%,#6f8094 40%,#c7b9d6 75%,#e7e0ec 100%)"></div>
  <svg class="abs" style="left:241px;top:240px" width="492" height="110" viewBox="0 0 492 110" aria-hidden="true">
    <path d="M0 30 C120 110 300 -20 492 40 L492 110 L0 110 Z" fill="var(--white)"/>
    <path d="M0 20 C120 95 300 -30 492 30 L492 60 C300 0 130 120 0 50 Z" fill="var(--green)"/>
    <path d="M180 60 C280 30 400 40 492 70 L492 78 C400 52 290 45 180 60 Z" fill="var(--green-dark)"/>
  </svg>

  <!-- Contact details -->
  <div class="contact" style="left:268px;top:363px;width:200px">
    <div class="place">Glimravex</div>
    <div>2210 Harbor Lane Fresno CA 93702</div>
    <div class="place" style="margin-top:9px">Glimravex Southwest</div>
    <div>8815 Alder Avenue, Suite 410 Fresno,<br>CA 93711</div>
    <div class="contact-row" style="margin-top:12px"><svg width="11" height="11" viewBox="0 0 11 11"><circle cx="5.5" cy="5.5" r="5.5" fill="var(--green)"/><circle cx="5.5" cy="5.5" r="3" fill="none" stroke="#fff" stroke-width="1"/></svg>www.glimravex.com</div>
    <div class="contact-row"><svg width="11" height="11" viewBox="0 0 11 11"><circle cx="5.5" cy="5.5" r="5.5" fill="var(--green)"/><rect x="2.5" y="3.5" width="6" height="4" fill="none" stroke="#fff" stroke-width="1"/></svg>appointments@glimravex.com</div>
    <div class="contact-row"><svg width="11" height="11" viewBox="0 0 11 11"><circle cx="5.5" cy="5.5" r="5.5" fill="var(--green)"/><path d="M3.5 3 L5 3 L5.3 4.6 L4.5 5.2 C5 6.2 5.6 6.8 6.6 7.3 L7.2 6.5 L8.5 6.9 L8.4 8.3 C5.5 8.3 3 5.8 3.5 3 Z" fill="#fff"/></svg>844-Glimravex</div>
  </div>

  <!-- Cover -->
  <div class="brand-name" style="left:503px;top:382px">Glimravex</div>
  <div class="rule" style="left:503px;top:442px;width:217px"></div>
  <div class="title" style="left:503px;top:448px">IV NUTRIENT THERAPY</div>
  <div class="tagline" style="left:503px;top:479px">REVITALIZE, RECHARGE AND REJUVENATE</div>
  <div class="rule" style="left:503px;top:495px;width:217px"></div>
</section>

<div class="side-label" style="left:408px;top:1150px">back</div>
<div class="side-label" style="left:645px;top:1150px">front</div>

</body>
</html>
```